Home page design for a live auction website.

Hi, we are looking at finding a good design for an auction website, only home page .. We will not be selling anything online, so the website will only be a portal where visitors can check about our company, upcoming auctions, online catalogues etc.
See attached our logo. Please use the same red that you see on the logo in the designs that you provide.
The final design should communicate high-end auction website, as we will be selling expensive piece of arts and antiques.
We should have a main frame where images of arts will circulate, with description of the art piece. just like on http://paris.vellmarotte-quisande.com/
(but with a better design overall) and of course a menu with different tabs, like "about us", "previous sales" "next sales", "contact" , "how to buy", "meet our specialists".

Target Market(s)

High end segment, who can afford to pay up to 250'000 for a piece of art

Industry/Entity Type

Online

Number of Pages Required

1 page

Requirements
Must have
• a frame with images rotating, just like on http://paris.vellmarotte-quisande.com/ . but the rest of the design should be more refined.
• we should also have a strong call to action, "Free online estimation", click here, estimation delivered in 48 hours"
Nice to have
• Tremaux Auctions, the brand should be well visible

```html
<!DOCTYPE html>
<html lang="en">
<head>
<meta charset="utf-8">
<title>Tremaux Auctions – Home</title>
<link href="https://fonts.googleapis.com/css2?family=Arimo:wght@400;700&family=Cormorant+Garamond:ital,wght@0,600;1,600&display=swap" rel="stylesheet">
<style>
:root{
  --red:#b3141b;
  --red-dark:#8e0f14;
  --ink:#2b2b2b;
  --muted:#555;
  --rule:#cfcfcf;
  --footer:#2a2a2a;
  --footer-text:#d8d8d8;
  --bg:#ffffff;
  --social-a:#3b5a9a;
  --social-b:#d23e2b;
  --social-c:#3aa7d8;
}
*{box-sizing:border-box;margin:0;padding:0}
html,body{width:1200px;height:2272px;overflow:hidden;background:var(--bg)}
body{position:relative;font-family:"Arimo",Arial,sans-serif;color:var(--ink)}
.abs{position:absolute}

/* header */
.brand{left:48px;top:18px;display:flex;align-items:center;gap:12px}
.brand-mark{width:44px;height:44px;border-radius:50%;background:var(--red)}
.brand-name{font-family:"Cormorant Garamond",Georgia,serif;font-weight:600;font-size:30px;color:var(--red);letter-spacing:1px;font-variant:small-caps}
.main-nav{right:48px;top:64px;display:flex;align-items:center}
.main-nav a{font-size:15px;color:var(--ink);text-decoration:none;padding:8px 18px;border-left:1px solid var(--rule)}
.main-nav a:first-child{border-left:none}
.main-nav a.active{background:var(--red);color:#fff;padding:8px 26px;border-radius:3px 3px 0 0}

/* hero */
.hero{left:48px;top:100px;width:1104px;height:540px;background:radial-gradient(circle at 48% 40%,#e8c98c 0%,#b87a3c 25%,#6a2a1c 60%,#3a1410 100%)}
.hero-caption{right:28px;bottom:40px;width:470px;height:130px;background:rgba(40,30,28,.82);color:#eee;padding:18px 24px;text-align:center}
.hero-caption h2{font-family:"Cormorant Garamond",Georgia,serif;font-weight:600;font-size:22px;margin-bottom:10px}
.hero-caption p{font-size:12px;line-height:17px;color:#ddd}

/* sections */
.section-title{left:48px;width:1104px;font-family:"Cormorant Garamond",Georgia,serif;font-style:italic;font-weight:600;font-variant:small-caps;font-size:38px;color:var(--ink);border-bottom:1px solid var(--rule);padding-bottom:4px}
.lot{width:300px;text-align:center}
.lot-photo{width:240px;height:220px;margin:0 auto;border-radius:4px}
.lot-title{font-size:15px;font-weight:700;margin-top:16px;line-height:20px}
.lot-btn{display:inline-block;margin-top:12px;background:var(--red);color:#fff;font-size:13px;font-weight:700;padding:7px 34px;border-radius:4px;text-decoration:none}

.intro{left:48px;top:1590px;width:1104px;font-size:17px;line-height:24px;color:var(--muted)}
.specialist{width:260px;text-align:center}
.portrait{width:210px;height:220px;margin:0 auto;background:linear-gradient(180deg,#ece9e6,#cfc7c0)}
.spec-name{font-size:16px;font-weight:700;margin-top:16px}
.spec-role{font-size:15px;font-style:italic;margin-top:6px}
.socials{display:flex;gap:14px;justify-content:center;margin-top:26px}
.socials span{width:40px;height:40px;border-radius:50%}
.s-a{background:var(--social-a)}.s-b{background:var(--social-b)}.s-c{background:var(--social-c)}

/* footer */
.site-footer{left:0;top:2112px;width:1200px;height:160px;background:var(--footer);color:var(--footer-text);font-size:13px}
.foot-col{position:absolute;top:20px}
.foot-col h4{color:var(--red);font-size:15px;margin-bottom:8px}
.foot-col li{list-style:none;line-height:20px}
.cta-click{color:#fff;font-weight:700;margin:4px 0 10px}
.newsletter{display:flex}
.newsletter input{width:190px;height:30px;border:none;padding:0 10px;font:13px "Arimo",Arial,sans-serif}
.newsletter button{height:30px;background:var(--red);color:#fff;border:none;padding:0 14px;font:700 12px "Arimo",Arial,sans-serif}
.follow{display:flex;gap:10px;margin-top:8px}
.follow span{width:28px;height:28px;border-radius:50%;background:var(--red)}
</style>
</head>
<body>

<header>
  <div class="abs brand"><span class="brand-mark"></span><span class="brand-name">Tremaux Auctions</span></div>
  <nav class="abs main-nav">
    <a class="active" href="#">Home</a>
    <a href="#">Previous Sales</a>
    <a href="#">Next Sales</a>
    <a href="#">How to Buy</a>
    <a href="#">Meet Our Specialists</a>
    <a href="#">Contact Us</a>
  </nav>
</header>

<section class="abs hero" role="img" aria-label="Close-up photograph of an antique gold pocket watch">
  <div class="abs hero-caption">
    <h2>Long Time Ago</h2>
    <p>This vintage gold pocket watch from a private European collection keeps its original case and dial, offered now with full provenance.</p>
  </div>
</section>

<h2 class="abs section-title" style="top:668px">Our Next Sales</h2>
<div class="abs lot" style="left:98px;top:730px">
  <div class="lot-photo" style="background:linear-gradient(180deg,#f2efe9,#c9b79a)" role="img" aria-label="Carved deer statue"></div>
  <p class="lot-title">Deer Statue from Africa<br>USD 1125.10 Only</p>
  <a class="lot-btn" href="#">View Details</a>
</div>
<div class="abs lot" style="left:450px;top:730px">
  <div class="lot-photo" style="background:linear-gradient(180deg,#f4eeea,#c89a86)" role="img" aria-label="Decorated copper jar"></div>
  <p class="lot-title">Decorated Jar from Morocco<br>USD 925.10 Only</p>
  <a class="lot-btn" href="#">View Details</a>
</div>
<div class="abs lot" style="left:802px;top:730px">
  <div class="lot-photo" style="background:linear-gradient(180deg,#f5eee2,#c79a4e)" role="img" aria-label="Gold plated bangles"></div>
  <p class="lot-title">Gold Plated Bangles<br>USD 1525.10 Only</p>
  <a class="lot-btn" href="#">View Details</a>
</div>

<h2 class="abs section-title" style="top:1052px">Our Previous Sales</h2>
<div class="abs lot" style="left:98px;top:1120px">
  <div class="lot-photo" style="height:250px;background:linear-gradient(180deg,#f3ede4,#8a6a3a)" role="img" aria-label="Antique gramophone"></div>
  <p class="lot-title">1800's Gramma Phone from Italy<br>USD 99.99 Only</p>
  <a class="lot-btn" href="#">Read Details</a>
</div>
<div class="abs lot" style="left:450px;top:1120px">
  <div class="lot-photo" style="height:250px;background:linear-gradient(180deg,#f5f0e4,#b49a5a)" role="img" aria-label="Brass butterfly statue"></div>
  <p class="lot-title">Butterfly Statue from Spain<br>USD 99.99 Only</p>
  <a class="lot-btn" href="#">Read Details</a>
</div>
<div class="abs lot" style="left:802px;top:1120px">
  <div class="lot-photo" style="height:250px;background:linear-gradient(180deg,#f6f4f2,#b8b4b0)" role="img" aria-label="Ceramic jar with a moulded face"></div>
  <p class="lot-title">Face Imprinted Jar from Europe<br>USD 112.10 Only</p>
  <a class="lot-btn" href="#">Read Details</a>
</div>

<h2 class="abs section-title" style="top:1530px">Meet Our Specialists</h2>
<p class="abs intro">Improved own provided blessing may peculiar domestic. Sight house has sex never. No visited raising gravity outward subject my cottage mr be. Hold do at tore in park feet near my case. Invitation at understood occasional sentiments insipidity inhabiting in. Off melancholy alteration principles old. Is do speedily kindness properly oh. Respect article painted cottage he is offices parlors.</p>

<div class="abs specialist" style="left:170px;top:1720px">
  <div class="portrait" role="img" aria-label="Portrait of a customer service specialist"></div>
  <p class="spec-name">Adrien Morel</p>
  <p class="spec-role">Customer Service Specialist</p>
  <div class="socials"><span class="s-a"></span><span class="s-b"></span><span class="s-c"></span></div>
</div>
<div class="abs specialist" style="left:470px;top:1720px">
  <div class="portrait" role="img" aria-label="Portrait of an accounts specialist"></div>
  <p class="spec-name">Adrien Morel</p>
  <p class="spec-role">Accounts Specialist</p>
  <div class="socials"><span class="s-a"></span><span class="s-b"></span><span class="s-c"></span></div>
</div>
<div class="abs specialist" style="left:800px;top:1720px">
  <div class="portrait" role="img" aria-label="Portrait of a purchasing manager"></div>
  <p class="spec-name">Elise Fontaine</p>
  <p class="spec-role">Purchasing Manager</p>
  <div class="socials"><span class="s-a"></span><span class="s-b"></span><span class="s-c"></span></div>
</div>

<footer class="abs site-footer">
  <div class="foot-col" style="left:120px">
    <h4>Quick Links</h4>
    <ul><li>Home</li><li>Previous Sales</li><li>Next Sales</li><li>How to Buy</li><li>Contact Us</li></ul>
  </div>
  <div class="foot-col" style="left:490px">
    <h4>Free Online Estimation</h4>
    <p class="cta-click">Click Here</p>
    <p>Estimated Delivery In 48 Hours</p>
  </div>
  <div class="foot-col" style="left:800px">
    <div class="newsletter"><input type="text" placeholder="Your Email"><button>Get Newsletter</button></div>
    <h4 style="margin-top:16px">Follow</h4>
    <div class="follow"><span></span><span></span><span></span><span></span></div>
  </div>
</footer>

</body>
</html>
```